New Business Card for Web Design/Internet Marketing Company

Looking for a great looking new business card. We are a 10 year old web design, internet marketing and website management company that works mostly with small businesses.

Our new card needs to better match the colors and style of our website, be bold, extremely usable and slightly edgy.

Target Market(s)

Small/Medium businesses that have websites

Industry/Entity Type

Internet

Requirements
Must have
• Front and back design, full color, rounded corners please

Must use the colors/style of our website (JPG provided)

INFO FOR CARDS (as readable as possible please)
Mark Pellow
President/CEO
mark@brightlanesites.com
Phone: 520-481-7093
Toll Free: 866-481-7093
Address: 4315 E. Kestrel Ave. Ste. 140, Saguaro Springs, AZ 85733

THINGS I WANT TO PROMOTE (if there is room):
1. Our Website - www.brightlanesites.com

2. Social Media
Twitter: @brightlanesites
Facebook: www.facebook.com/brightlanesites

3. Our Services
Web Design
Internet Marketing
Website Management

```html
<!DOCTYPE html>
<html lang="en">
<head>
<meta charset="utf-8">
<title>Bright Lane Sites – Business Card</title>
<link rel="stylesheet" href="https://fonts.googleapis.com/css2?family=Source+Sans+3:ital,wght@0,400;0,600;0,700;1,400;1,600;1,700&display=swap">
<style>
  :root {
    --backdrop: #3b3b3d;
    --blue: #1a8fce;
    --blue-deep: #0b6fae;
    --blue-light: #35b4ee;
    --orange: #f0832a;
    --white: #ffffff;
    --grey: #6d6e70;
    --text-font: "Source Sans 3", "Myriad Pro", Arial, sans-serif;
  }
  * { box-sizing: border-box; margin: 0; padding: 0; }
  html, body { width: 1200px; height: 900px; overflow: hidden; }
  body { background: var(--backdrop); font-family: var(--text-font); position: relative; }

  .card {
    position: absolute; top: 300px; width: 525px; height: 300px;
    border-radius: 22px; overflow: hidden; background: var(--white);
  }
  .card--front { left: 58px; }
  .card--back { left: 617px; }
  .card__bg { position: absolute; inset: 0; width: 100%; height: 100%; }

  .brand-name {
    font-weight: 700; font-size: 40px; letter-spacing: -0.5px; line-height: 1;
    display: inline-flex; align-items: center; gap: 10px; white-space: nowrap;
  }
  .brand-dot { width: 22px; height: 22px; border-radius: 50%; display: inline-block; }
  .tagline { font-size: 14px; margin-top: 4px; white-space: nowrap; }

  /* Front */
  .front__brand { position: absolute; top: 100px; left: 0; right: 0; text-align: center; }
  .front .brand-name { color: var(--white); }
  .front .brand-dot { background: var(--white); }
  .front .tagline { color: var(--white); }
  .front__services {
    position: absolute; top: 180px; left: 0; right: 0; text-align: center;
    color: var(--white); font-style: italic; font-size: 12px;
  }
  .front__web {
    position: absolute; top: 203px; left: 0; right: 0; text-align: center;
    color: var(--white); font-size: 15px; letter-spacing: 2.5px;
  }
  .social {
    position: absolute; top: 266px; display: flex; align-items: center; gap: 8px;
    color: var(--blue); font-style: italic; font-size: 12.5px; text-transform: uppercase;
  }
  .social--page { left: 77px; }
  .social--handle { left: 300px; }
  .social__mark { width: 15px; height: 15px; border-radius: 2px; background: var(--orange); }

  /* Back */
  .back__brand { position: absolute; top: 58px; left: 48px; }
  .back .brand-name { color: var(--blue); font-size: 42px; }
  .back .brand-dot { background: var(--orange); width: 24px; height: 24px; }
  .back .tagline { color: var(--grey); font-size: 15px; margin-left: 34px; }
  .contact-person { position: absolute; top: 197px; left: 53px; color: var(--white); }
  .contact-person__name { font-style: italic; font-weight: 700; font-size: 18px; line-height: 1.1; }
  .contact-person__role { font-size: 13px; margin-top: 1px; }
  .contact-person__address { font-size: 13px; margin-top: 10px; line-height: 1.55; white-space: nowrap; }
  .contact-lines { position: absolute; top: 199px; left: 298px; list-style: none; color: var(--white); font-size: 13px; line-height: 20px; white-space: nowrap; }
  .contact-lines__label { color: var(--orange); }
</style>
</head>
<body>

<section class="card card--front front" aria-label="Card front">
  <svg class="card__bg" viewBox="0 0 525 300" preserveAspectRatio="none" aria-hidden="true">
    <defs>
      <radialGradient id="front-blue" cx="0.5" cy="0.32" r="0.7">
        <stop offset="0" stop-color="#3cbcf2"/>
        <stop offset="0.55" stop-color="#1a8fce"/>
        <stop offset="1" stop-color="#0b6fae"/>
      </radialGradient>
    </defs>
    <rect width="525" height="300" fill="url(#front-blue)"/>
    <path d="M0,228 C150,246 350,242 525,208 L525,300 L0,300 Z" fill="#ffffff"/>
    <path d="M190,246 C340,246 450,232 525,210 L525,221 C450,240 340,252 190,246 Z" fill="#f0832a"/>
  </svg>
  <div class="front__brand">
    <div class="brand-name"><span class="brand-dot"></span>Bright Lane Sites</div>
    <div class="tagline">Sites that Work Harder</div>
  </div>
  <p class="front__services">Web Design &nbsp;/&nbsp; Internet Marketing &nbsp;/&nbsp; Website Management</p>
  <p class="front__web">www.brightlanesites.com</p>
  <div class="social social--page"><span class="social__mark"></span>/brightlanesites</div>
  <div class="social social--handle"><span class="social__mark"></span>@brightlanesites</div>
</section>

<section class="card card--back back" aria-label="Card back">
  <svg class="card__bg" viewBox="0 0 525 300" preserveAspectRatio="none" aria-hidden="true">
    <defs>
      <radialGradient id="back-blue" cx="0.28" cy="0.7" r="0.8">
        <stop offset="0" stop-color="#35b4ee"/>
        <stop offset="0.55" stop-color="#1a8fce"/>
        <stop offset="1" stop-color="#0b6fae"/>
      </radialGradient>
    </defs>
    <path d="M0,150 C160,152 360,162 525,134 L525,300 L0,300 Z" fill="url(#back-blue)"/>
    <path d="M170,164 C330,166 450,154 525,136 L525,146 C450,164 330,172 170,164 Z" fill="#f0832a"/>
  </svg>
  <div class="back__brand">
    <div class="brand-name"><span class="brand-dot"></span>Bright Lane Sites</div>
    <div class="tagline">Sites that Work Harder</div>
  </div>
  <div class="contact-person">
    <p class="contact-person__name">Mark Pellow</p>
    <p class="contact-person__role">President/CEO</p>
    <p class="contact-person__address">4315 E. Kestrel Ave. Ste. 140,<br>Saguaro Springs, AZ 85733</p>
  </div>
  <ul class="contact-lines">
    <li><span class="contact-lines__label">p:</span> 520-481-7093</li>
    <li><span class="contact-lines__label">t:</span> 866-481-7093</li>
    <li><span class="contact-lines__label">e:</span> mark@brightlanesites.com</li>
    <li><span class="contact-lines__label">w:</span> www.brightlanesites.com</li>
  </ul>
</section>

</body>
</html>
```